Professional modern business card design

A business card for my nutrition business, wanting a professional look, with info clearly visible. Open to using logo colours too.

Would like key info on the front -
logo
my name and qualifications
email
phone number

and just an enlarged logo again / image on the back.

```html
<!DOCTYPE html>
<html lang="en">
<head>
<meta charset="utf-8">
<title>Fernleaf Nutrition – Business Card</title>
<link rel="stylesheet" href="https://fonts.googleapis.com/css2?family=Montserrat:wght@400;600;700&family=Open+Sans:wght@700&display=swap">
<style>
  :root {
    --navy: #0d2a40;
    --navy-deep: #0a2236;
    --lime: #d4db2f;
    --lime-text: #c2cc23;
    --white: #ffffff;
    --ink: #2b2b2b;
    --backdrop: #e9e7e3;
    --logo-faint: #0a1c2b;
  }
  * { margin: 0; padding: 0; box-sizing: border-box; }
  html, body { width: 900px; height: 1200px; overflow: hidden; }
  body {
    background: var(--backdrop);
    position: relative;
    font-family: "Montserrat", sans-serif;
  }
  .card {
    position: absolute;
    left: 80px;
    width: 742px;
    height: 440px;
    border-radius: 40px;
    overflow: hidden;
  }
  .card--front { top: 132px; background: var(--white); }
  .card--back { top: 638px; background: var(--navy); }

  .front-wave { position: absolute; inset: 0; width: 742px; height: 440px; }

  .brand-name {
    position: absolute;
    left: 66px;
    top: 52px;
    font-family: "Open Sans", sans-serif;
    font-weight: 700;
    font-size: 58px;
    line-height: 66px;
    color: var(--navy);
  }
  .holder {
    position: absolute;
    right: 47px;
    top: 52px;
    text-align: right;
  }
  .holder__name {
    font-weight: 700;
    font-size: 25px;
    color: var(--lime-text);
    line-height: 32px;
  }
  .holder__role {
    font-weight: 400;
    font-size: 16px;
    color: var(--ink);
    line-height: 22px;
  }
  .contact {
    position: absolute;
    left: 62px;
    top: 350px;
    list-style: none;
    color: var(--white);
    font-size: 16px;
    line-height: 22px;
  }
  .contact li { display: flex; align-items: center; gap: 10px; }
  .contact svg { width: 14px; height: 14px; fill: var(--white); flex: none; }

  .brand-name--large {
    position: absolute;
    left: 170px;
    top: 100px;
    font-family: "Open Sans", sans-serif;
    font-weight: 700;
    font-size: 92px;
    line-height: 108px;
    color: var(--logo-faint);
  }
  .back-band {
    position: absolute;
    left: 0; right: 0; bottom: 0;
    height: 13px;
    background: var(--lime);
  }
</style>
</head>
<body>
  <section class="card card--front" aria-label="Business card front">
    <svg class="front-wave" viewBox="0 0 742 440" aria-hidden="true">
      <path d="M0,333 C90,292 200,270 300,292 C400,315 470,378 560,386 C640,393 700,362 742,328 L742,440 L0,440 Z" fill="var(--lime)"/>
      <path d="M490,378 C600,402 695,372 742,302 L742,322 C700,378 615,398 490,378 Z" fill="var(--navy)"/>
    </svg>

    <div class="brand-name">Fernleaf<br>Nutrition</div>

    <div class="holder">
      <p class="holder__name">Harriet Lowe</p>
      <p class="holder__role">Specialist Rehabilitation Dietitian</p>
    </div>

    <ul class="contact">
      <li>
        <svg viewBox="0 0 16 16" aria-hidden="true"><path d="M2 5c0-2 2-3 6-3s6 1 6 3v1h-3V5H5v1H2zM4 7h8l2 6H2z"/></svg>
        <span>07700900318</span>
      </li>
      <li>
        <svg viewBox="0 0 16 16" aria-hidden="true"><path d="M1 3h14v2L8 9 1 5zM1 7l7 4 7-4v6H1z"/></svg>
        <span>harriet@fernleafnutrition.co.uk</span>
      </li>
      <li>
        <svg viewBox="0 0 16 16" aria-hidden="true"><circle cx="8" cy="8" r="7"/></svg>
        <span>www.fernleafnutrition.co.uk</span>
      </li>
    </ul>
  </section>

  <section class="card card--back" aria-label="Business card back">
    <div class="brand-name--large">Fernleaf<br>Nutrition</div>
    <div class="back-band"></div>
  </section>
</body>
</html>
```